TuneNest - Music Industry App needs a top quality wordpress homepage

We need a modern responsive wordpress homepage built. Our website will only feature one page with the goal to get people to sign up to our app. A word document has been uploaded outlining the page content/sections.

Once the homepage is finalised, I will also need 2 landing pages built as part of this competition. It will be very similar to the homepage with the same layout etc but just feature different images and content. The homepage is for anyone (artists and venues) to find out about us but the landing pages will be artist or venue specific.

The completed work must be delivered as an exportable file into wordpress and be designed properly so no more work is needed to begin utilising as the actual website. The images used must be setup correctly for speed and quality also.

Target Market(s)

Venues and Artists.

Coding

Coded - Design and coding required

Requirements
Must have
• UPDATE: High Res Logo files attached
• Must be a modern looking website and be responsive. Must look good across all devices from desktop, to mobile and tablet. Needs to be very high quality.
• Please see the attached logo - I am waiting for the final high quality version and will reupload when complete but this will be enough to get you started for now. The website must have a dark base colour and have red/white elements to match the logo. The red colour used MUST match the red colour used in the logo.
• Please have a go at creating it how you think is best and provide feedback from there. I am leaving it very open to the designers so I can get the best website possible and lots of different ideas etc.

```html
<!DOCTYPE html>
<html lang="en">
<head>
<meta charset="utf-8">
<title>TuneNest – Book live music</title>
<link href="https://fonts.googleapis.com/css2?family=Quicksand:wght@500;700&family=Lato:ital,wght@0,400;0,700;1,400&display=swap" rel="stylesheet">
<style>
:root{
  --red:#e3101e;
  --red-deep:#c40c18;
  --white:#ffffff;
  --ink:#2b0c2a;
  --plum:#3a1236;
  --plum-mid:#4a1a43;
  --card:rgba(120,70,110,.35);
  --line:rgba(255,255,255,.28);
  --field:rgba(255,255,255,.14);
  --text-soft:rgba(255,255,255,.88);
}
*{box-sizing:border-box;margin:0;padding:0}
html,body{width:1200px;height:3802px;overflow:hidden}
body{position:relative;background:var(--ink);color:var(--white);font-family:"Lato",sans-serif}
.abs{position:absolute}
.head{font-family:"Quicksand",sans-serif}
.center{text-align:center}

/* hero */
.hero{left:0;top:0;width:1200px;height:666px;background:
  radial-gradient(ellipse 420px 260px at 600px 170px,rgba(230,70,50,.75),transparent 70%),
  linear-gradient(180deg,#7a1d1e 0%,#5a1526 45%,#24121f 100%)}
.nav-logo{left:77px;top:24px;display:flex;align-items:center;gap:10px;font-family:"Quicksand",sans-serif;font-weight:700;font-size:32px}
.nav-logo .dot{width:36px;height:36px;border-radius:50%;background:var(--white)}
.nav{left:327px;top:36px;display:flex;gap:27px;font-size:13px;letter-spacing:.2px}
.btn-signup{left:957px;top:22px;width:166px;height:46px;background:var(--white);color:var(--red);border-radius:3px;font-family:"Quicksand",sans-serif;font-weight:700;font-size:17px;display:flex;align-items:center;justify-content:center}
.hero-title{left:0;width:1200px;top:205px;font-weight:700;font-size:46px;letter-spacing:-.5px}
.hero-sub{left:0;width:1200px;top:276px;font-size:21px;color:var(--text-soft)}
.hero-box{left:267px;top:351px;width:666px;height:166px;border:1px solid var(--line)}
.hero-box-label{left:0;width:1200px;top:382px;font-size:19px}
.input{background:var(--white);border-radius:24px;color:#777;font-size:14px;display:flex;align-items:center;padding-left:23px}
.pill-red{background:var(--red);border-radius:24px;font-family:"Quicksand",sans-serif;font-weight:700;font-size:17px;display:flex;align-items:center;justify-content:center}

/* how + why */
.works{left:0;top:666px;width:1200px;height:1177px;background:
  linear-gradient(180deg,#9d2a2c 0%,#6e1f34 30%,#44173e 60%,#3a1338 100%)}
.sec-title{left:0;width:1200px;font-family:"Quicksand",sans-serif;font-weight:500;font-size:40px}
.sec-title b{font-weight:700}
.phone{left:221px;top:819px;width:239px;height:475px;border-radius:30px;background:linear-gradient(180deg,#5a4a5e,#2a2030);border:4px solid #d9d9de}
.steps-line{left:599px;top:899px;height:313px;border-left:2px dotted rgba(255,255,255,.5)}
.step-num{width:62px;height:62px;border-radius:50%;border:1.5px solid rgba(255,255,255,.8);color:var(--red);font-size:22px;display:flex;align-items:center;justify-content:center;background:rgba(60,15,40,.35)}
.step-text{left:658px;width:372px;font-size:14px;line-height:25px}
.card{top:1464px;width:239px;height:291px;background:var(--card)}
.card-icon{position:absolute;left:83px;top:44px;width:73px;height:73px;border-radius:50%;border:1.5px solid var(--red);display:flex;align-items:center;justify-content:center}
.card h3{position:absolute;top:136px;width:100%;text-align:center;font-family:"Quicksand",sans-serif;font-weight:700;font-size:22px}
.card p{position:absolute;top:177px;left:22px;right:22px;text-align:center;font-size:14px;line-height:25px}

/* launch */
.launch{left:0;top:1843px;width:1200px;height:771px;background:
  linear-gradient(180deg,#3a1338 0%,#4c1a3e 55%,#8a2a30 100%)}
.launch-note{left:170px;width:860px;top:1914px;font-style:italic;font-size:17px;line-height:31px}
.panel{top:2035px;width:499px;height:487px;border:1px solid var(--line);background:rgba(70,25,60,.35)}
.panel h3{position:absolute;top:38px;width:100%;text-align:center;font-family:"Quicksand",sans-serif;font-weight:700;font-size:31px}
.panel ul{position:absolute;top:88px;left:32px;right:32px;list-style:none}
.panel li{text-align:center;font-size:14px;line-height:25px;border-bottom:1px solid var(--line);display:flex;align-items:center;justify-content:center}
.panel li:last-child{border-bottom:none}

/* cta */
.cta{left:0;top:2614px;width:1200px;height:146px;background:var(--red)}
.cta-title{left:78px;top:2668px;width:630px;white-space:nowrap;font-family:"Quicksand",sans-serif;font-weight:700;font-size:25px;letter-spacing:-.2px}
.cta-form{left:728px;top:2664px;width:394px;height:46px;border:2px solid var(--white);border-radius:24px;background:var(--white)}

/* about */
.about{left:0;top:2760px;width:1200px;height:354px;background:linear-gradient(180deg,#7a2234 0%,#5a1c40 100%)}
.about-lead{left:250px;width:700px;top:2888px;font-size:19px;line-height:30px}
.about-body{left:250px;width:700px;top:2970px;font-size:14px;line-height:25px}

/* contact */
.contact{left:0;top:3114px;width:1200px;height:625px;background:linear-gradient(180deg,#3a1338,#4a1842)}
.singer{left:635px;top:3114px;width:565px;height:625px;background:radial-gradient(ellipse 230px 300px at 260px 330px,#7a3a7a,#4a1c48 70%,transparent)}
.field{left:77px;width:499px;height:46px;border-radius:24px;background:var(--field);font-size:14px;display:flex;align-items:center;padding-left:32px}
.footer{left:0;top:3739px;width:1200px;height:63px;background:var(--red);font-size:13px;display:flex;align-items:center;justify-content:center}
</style>
</head>
<body>

<section class="abs hero" role="img" aria-label="Concert crowd with raised hands under red stage lights"></section>
<div class="abs nav-logo"><span class="dot"></span>TuneNest</div>
<nav class="abs nav"><span>HOW IT WORKS?</span><span>WHY TUNE NEST</span><span>VENUES</span><span>ARTIST</span><span>ABOUT</span><span>CONTACT</span></nav>
<div class="abs btn-signup">SIGN UP NOW</div>
<h1 class="abs hero-title head center">ZOOMCAB FOR LIVE MUSIC</h1>
<p class="abs hero-sub center">TuneNest connects venues with artists to make booking gigs simple</p>
<div class="abs hero-box"></div>
<p class="abs hero-box-label center">Sign up now for FREE</p>
<div class="abs input" style="left:314px;top:428px;width:394px;height:47px">Enter your email</div>
<div class="abs pill-red" style="left:720px;top:428px;width:166px;height:47px">SUBSCRIBE</div>

<section class="abs works" role="img" aria-label="Dim stage background with a microphone"></section>
<h2 class="abs sec-title center" style="top:720px"><b>How TuneNest</b> Works</h2>
<div class="abs phone" role="img" aria-label="Smartphone showing the app confirmation screen"></div>
<div class="abs steps-line"></div>
<div class="abs step-num" style="left:568px;top:837px">1</div>
<div class="abs step-num" style="left:568px;top:930px">2</div>
<div class="abs step-num" style="left:568px;top:1024px">3</div>
<div class="abs step-num" style="left:568px;top:1117px">4</div>
<div class="abs step-num" style="left:568px;top:1212px">5</div>
<p class="abs step-text" style="top:855px">Artists and venues sign up for free and create a profile</p>
<p class="abs step-text" style="top:948px">Venues search for an artist for their upcoming gigs</p>
<p class="abs step-text" style="top:1030px">Venues request a quote and communicate with the artist direct</p>
<p class="abs step-text" style="top:1124px">The gig is booked in once payment is provided by the venue.</p>
<p class="abs step-text" style="top:1218px">Upon completion the money is paid to the artist within 48 hours or less.</p>

<h2 class="abs sec-title center" style="top:1372px"><b>Why TuneNest?</b></h2>
<div class="abs card" style="left:77px">
  <div class="card-icon"><svg width="26" height="30" viewBox="0 0 26 30"><rect x="2" y="1" width="22" height="28" rx="2" fill="#e3101e"/><path d="M7 9h12M7 14h12M7 19h12" stroke="#5a2a4c" stroke-width="2"/></svg></div>
  <h3>Simple</h3><p>TuneNest makes gig booking easy for both the venue and artist.</p>
</div>
<div class="abs card" style="left:345px">
  <div class="card-icon"><svg width="32" height="32" viewBox="0 0 32 32"><circle cx="24" cy="7" r="5" fill="#e3101e"/><circle cx="8" cy="16" r="5" fill="#e3101e"/><circle cx="24" cy="25" r="5" fill="#e3101e"/><path d="M24 7L8 16L24 25" stroke="#e3101e" stroke-width="3" fill="none"/></svg></div>
  <h3>Connect</h3><p>Join the TuneNest community which is full of amazing artists and venues.</p>
</div>
<div class="abs card" style="left:614px">
  <div class="card-icon"><svg width="26" height="32" viewBox="0 0 26 32"><path d="M6 14V9a7 7 0 0 1 14 0v5" stroke="#e3101e" stroke-width="3.5" fill="none"/><rect x="2" y="14" width="22" height="17" rx="2" fill="#e3101e"/></svg></div>
  <h3>Protection</h3><p>Everyone is protected with our complimentary dispute resolutions</p>
</div>
<div class="abs card" style="left:883px">
  <div class="card-icon"><svg width="32" height="32" viewBox="0 0 32 32"><path d="M3 4h13l13 13-12 12L4 16z" fill="#e3101e"/><circle cx="10" cy="10" r="2.6" fill="#5a2a4c"/></svg></div>
  <h3>Price</h3><p>Get the best rate possible with TuneNest only receiving 5% of the artists fee</p>
</div>

<section class="abs launch" role="img" aria-label="Festival crowd making heart shapes with their hands"></section>
<p class="abs launch-note center">TuneNest is not yet ready to host gigs as we're currently working on building our artists. We are launching for venues in Q4 2019. Pre-register now to keep informed and be one of the first people to use our platform.</p>
<div class="abs panel" style="left:77px">
  <h3>Venues</h3>
  <ul>
    <li style="height:56px">TuneNest is a 100% FREE service for all venues - you pay us nothing!</li>
    <li style="height:88px">Get instant access to hundreds of artists around your local community</li>
    <li style="height:68px">Simple booking process with a money back guarantee</li>
    <li style="height:88px">All genres to suit any venue from a pub to a wedding or even a nightclub</li>
    <li style="height:68px">Communicate directly with the artist and negotiate the price</li>
  </ul>
</div>
<div class="abs panel" style="left:624px">
  <h3>Artists</h3>
  <ul>
    <li style="height:56px">Sign up to TuneNest for FREE and get yourself in front of venues</li>
    <li style="height:88px">Only pay us if you get a gig - we only get 5% of the fee you charge the venue</li>
    <li style="height:84px">All genres and artists welcome - as long as you're experienced and professional</li>
    <li style="height:64px">Get paid within 48 hours or less after the gig guaranteed!</li>
    <li style="height:88px">Negotiate your price and don't pay huge agent fees to ensure you earn top dollar</li>
  </ul>
</div>

<section class="abs cta"></section>
<h2 class="abs cta-title">Sign up and create your TuneNest profile now</h2>
<div class="abs cta-form"></div>
<div class="abs" style="left:750px;top:2676px;font-size:14px;color:#777">Enter your email</div>
<div class="abs pill-red" style="left:984px;top:2668px;width:134px;height:38px;font-size:16px">REGISTER</div>

<section class="abs about" role="img" aria-label="Close-up of a stage microphone in red light"></section>
<h2 class="abs sec-title center" style="top:2815px"><b>About</b> TuneNest</h2>
<p class="abs about-lead center">Lorem Ipsum is simply dummy text of the printing and typesetting industry Lorem Ipsum has been the industry's standard dummy text ever since.</p>
<p class="abs about-body center">It has survived not only five centuries, but also the leap into electronic typesetting, remaining essentially unchanged. It was popularised in the 1960s with the release of Typeline sheets containing Lorem Ipsum passages, and more recently with desktop publishing software like PageForge including .</p>

<section class="abs contact"></section>
<div class="abs singer" role="img" aria-label="Singer performing on stage holding a microphone"></div>
<h2 class="abs sec-title" style="left:78px;top:3180px;width:auto"><b>Contact</b> us</h2>
<svg class="abs" style="left:76px;top:3262px" width="20" height="28" viewBox="0 0 20 28"><path d="M10 0a10 10 0 0 1 10 10c0 7-10 18-10 18S0 17 0 10A10 10 0 0 1 10 0z" fill="#e3101e"/><circle cx="10" cy="10" r="4" fill="#3a1338"/></svg>
<p class="abs" style="left:121px;top:3255px;width:250px;font-size:14px;line-height:25px">Lorem Ipsum is simply dummy text of the printing and typesetting industry.</p>
<svg class="abs" style="left:410px;top:3265px" width="22" height="22" viewBox="0 0 24 24"><path d="M6.6 10.8a15 15 0 0 0 6.6 6.6l2.2-2.2c.3-.3.7-.4 1-.2 1.1.4 2.3.6 3.6.6.6 0 1 .4 1 1V20c0 .6-.4 1-1 1A17 17 0 0 1 3 4c0-.6.4-1 1-1h3.5c.6 0 1 .4 1 1 0 1.3.2 2.5.6 3.6.1.3 0 .7-.2 1z" fill="#e3101e"/></svg>
<p class="abs" style="left:453px;top:3263px;font-size:20px;font-weight:700">555 014 2290</p>
<div class="abs field" style="top:3348px">Name</div>
<div class="abs field" style="top:3410px">Email</div>
<div class="abs field" style="top:3472px">Phone</div>
<div class="abs field" style="top:3534px">Subject</div>
<div class="abs pill-red" style="left:77px;top:3597px;width:167px;height:46px;font-size:18px">SUBMIT</div>

<footer class="abs footer">©TuneNest. 2019 - All Rights Reserved.</footer>
</body>
</html>
```